Presentation Flyer for Married Couple at night separate business owners by day

I would like a flyer to use to advertise free presentations put on by husband and I. I (Danielle Vorhagen) am an estate planning attorney that works for PMR Law. My husband (Ray Vorhagen) is a financial planner that works for Belvorne Financial Planning. Would love it to be funny but serious. At night we are a married couple of 4 children, by day we individually work with people helping them protect their assets and their families.
Goal is for this to be used for multiple events.
Things to include: Food will be provided, Raffle for $500 off an Estate Plan Package
Topics to be covered in Seminar:
Estate & Financial Planning Essentials

Protect Your Future
Build a strong financial foundation with emergency funds, retirement planning, and smart investment strategies that match your goals.

Secure Your Legacy
Learn about wills, trusts, and powers of attorney - the essential documents everyone needs to protect their family's future.

Guard Your Assets
Understand the right insurance coverage to protect yourself and your loved ones, from life insurance to long-term care options.

Transfer Wealth Wisely
Discover tax-efficient strategies for passing assets to the next generation and making the most of your charitable giving.

```html
<!DOCTYPE html>
<html lang="en">
<head>
<meta charset="utf-8">
<title>Estate &amp; Financial Planning Seminar Flyer</title>
<link rel="stylesheet" href="https://fonts.googleapis.com/css2?family=Gelasio:wght@400;500&family=Poppins:wght@400;500&display=swap">
<style>
  :root {
    --teal: #137070;
    --ink: #1b1b1b;
    --paper: #f5f6f8;
    --white: #ffffff;
    --brick-light: #c99670;
    --brick-dark: #8a5a3c;
    --suit: #2a3448;
  }
  html, body {
    margin: 0;
    width: 1200px;
    height: 1200px;
    overflow: hidden;
    background: var(--paper);
  }
  .flyer {
    position: absolute;
    left: 176px;
    top: 0;
    width: 848px;
    height: 1200px;
    background: var(--paper);
    overflow: hidden;
    font-family: "Poppins", sans-serif;
    color: var(--ink);
  }
  .hero-photo {
    position: absolute;
    left: 0; top: 0;
    width: 848px; height: 580px;
    background:
      linear-gradient(180deg, rgba(0,0,0,0) 55%, rgba(30,34,48,0.75) 100%),
      linear-gradient(100deg, #d9cfc2 0%, var(--brick-light) 35%, #b9825c 65%, var(--brick-dark) 100%);
  }
  .brand {
    position: absolute;
    left: 51px; top: 118px;
    display: flex;
    align-items: center;
    gap: 8px;
    font-family: "Poppins", sans-serif;
    font-weight: 500;
    font-size: 17px;
    color: var(--white);
    letter-spacing: 0.5px;
  }
  .brand-mark {
    width: 14px; height: 14px;
    background: var(--teal);
  }
  .wave {
    position: absolute;
    left: 0; top: 0;
    width: 848px; height: 1200px;
  }
  .headline {
    position: absolute;
    left: 49px; top: 560px;
    margin: 0;
    font-family: "Gelasio", serif;
    font-weight: 400;
  }
  .headline-lead {
    display: block;
    font-size: 34px;
    letter-spacing: 2.6px;
    color: var(--ink);
    white-space: nowrap;
  }
  .headline-lead .offer { color: var(--teal); }
  .headline-prize {
    display: block;
    margin-top: -2px;
    font-size: 56px;
    font-weight: 500;
    letter-spacing: 2.4px;
    color: var(--teal);
  }
  .topics-title {
    position: absolute;
    left: 49px; top: 710px;
    margin: 0;
    font-size: 24px;
    font-weight: 500;
    line-height: 30px;
    letter-spacing: 0.8px;
  }
  .topics {
    position: absolute;
    left: 49px; top: 808px;
    width: 760px;
    margin: 0; padding: 0;
    list-style: none;
  }
  .topic {
    position: relative;
    padding-left: 22px;
    margin-bottom: 22px;
  }
  .topic::before {
    content: "";
    position: absolute;
    left: 2px; top: 9px;
    width: 11px; height: 11px;
    border-radius: 50%;
    background: var(--teal);
  }
  .topic-name {
    margin: 0;
    font-size: 20px;
    font-weight: 500;
    line-height: 28px;
    color: var(--teal);
  }
  .topic-text {
    margin: 0;
    font-size: 16.5px;
    line-height: 21px;
    color: var(--ink);
  }
</style>
</head>
<body>
  <main class="flyer">
    <div class="hero-photo" role="img" aria-label="Portrait photo of the presenting couple smiling in front of a brick wall"></div>

    <div class="brand">
      <span class="brand-mark"></span>
      <span>Belvorne Financial LLC</span>
    </div>

    <svg class="wave" viewBox="0 0 1150 1627" preserveAspectRatio="none" aria-hidden="true">
      <path fill="#ffffff" d="M0,650 C120,580 250,550 380,560 C560,575 700,660 880,680 C1000,690 1090,630 1150,578 V1627 H0 Z"/>
      <path fill="#137070" d="M0,690 C100,610 230,590 380,600 C560,615 720,700 900,705 C1010,705 1100,640 1150,600 V1627 H0 Z"/>
      <path fill="#f5f6f8" d="M0,742 C80,660 200,630 350,640 C560,655 700,735 880,748 C1000,755 1100,705 1150,640 V1627 H0 Z"/>
    </svg>

    <h1 class="headline">
      <span class="headline-lead">Food will be provided Raffle for <span class="offer">$500 off</span></span>
      <span class="headline-prize">an Estate Plan Package</span>
    </h1>

    <h2 class="topics-title">Topics to be covered in the Seminar:<br>Estate &amp; Financial Planning Essentials</h2>

    <ul class="topics">
      <li class="topic">
        <p class="topic-name">Protect Your Future</p>
        <p class="topic-text">Build a strong financial foundation with emergency funds, retirement planning, and smart investment strategies that match your goals.</p>
      </li>
      <li class="topic">
        <p class="topic-name">Secure Your Legacy</p>
        <p class="topic-text">Learn about wills, trusts, and powers of attorney - the essential documents everyone needs to protect their family's future.</p>
      </li>
      <li class="topic">
        <p class="topic-name">Guard Your Assets</p>
        <p class="topic-text">Understand the right insurance coverage to protect yourself and your loved ones, from life insurance to long-term care options.</p>
      </li>
      <li class="topic">
        <p class="topic-name">Transfer Wealth Wisely</p>
        <p class="topic-text">Discover tax-efficient strategies for passing assets to the next generation and making the most of your charitable giving.</p>
      </li>
    </ul>
  </main>
</body>
</html>
```